Lumo Cellar Traders needs a new business card design

Colour theme: Gold + Red preferred
Front side: Main logo with my details as below;
Back side: Theme of some wine glasses or bottles, maybe different color of log together
Lumo Cellar Traders

Leo Park
박 성민 (this is Korean character) on the English typying board: qkr tjdals
Managing Director

Suite 7/5 Harlow Rd
Bayfield WA 6923
Tel) +61(8) 6027 3518
Mob) +61(412) 305 276

leo.park@lumocellartraders.example
lumocellar@lumocellartraders.example
www.lumocellartraders.example

Target Market(s)

Asian Market

Industry/Entity Type

Business

Contact Information for Business Card

Lumo Cellar Traders

Leo Park
박 성민 (this is Korean character) English typying: qkr tjdals
Managing Director

Suite 7/5 Harlow Rd
Bayfield WA 6923
Tel) +61(8) 6027 3518
Mob) +61(412) 305 276

Font styles to use
Serif
Decorative

Colors
ec1f27
f78f21
f04a50
faa54b
cadf82
abd036

Requirements
Must have
• Company Logo & wine theme
Nice to have
• Very simple & modern
Should not have
• No Red Color on the name of Leo Park or 박 성민
• No traditional looking. young and modern look preferred

```html
<!DOCTYPE html>
<html lang="en">
<head>
<meta charset="utf-8">
<title>Lumo Cellar Traders – Business Card</title>
<link rel="stylesheet" href="https://fonts.googleapis.com/css2?family=Open+Sans:wght@400;600;700&display=swap">
<style>
  :root {
    --page-bg: #ececec;
    --card-bg: #ffffff;
    --wave-red: #f04a50;
    --wave-red-light: #f7636a;
    --wave-gold: #faa54b;
    --ink: #2b2b2b;
    --ink-soft: #444444;
    --brand-red: #ec1f27;
    --brand-faint: #e7c9b8;
  }
  * { box-sizing: border-box; margin: 0; padding: 0; }
  html, body {
    width: 1200px; height: 800px; overflow: hidden;
    background: var(--page-bg);
    font-family: "Open Sans", Arial, sans-serif;
    color: var(--ink);
  }
  .canvas { position: relative; width: 1200px; height: 800px; }

  .card {
    position: absolute;
    background: var(--card-bg);
    overflow: hidden;
    box-shadow: 0 4px 14px rgba(0,0,0,0.12);
  }
  .card-front { left: 80px; top: 240px; width: 560px; height: 320px; }
  .card-back  { left: 760px; top: 120px; width: 320px; height: 560px; }

  .wave { position: absolute; inset: 0; width: 100%; height: 100%; }

  .holder {
    position: absolute; right: 40px; top: 28px; text-align: right;
  }
  .holder-name { font-size: 26px; font-weight: 700; line-height: 1.1; letter-spacing: 0.2px; }
  .holder-title { font-size: 9px; color: var(--ink-soft); margin-top: 1px; }

  .contact-list {
    position: absolute; right: 40px; top: 92px;
    list-style: none; text-align: right;
  }
  .contact-item {
    display: flex; align-items: center; justify-content: flex-end;
    gap: 8px; font-size: 11px; line-height: 1; height: 22px; color: var(--ink-soft);
  }
  .contact-icon { width: 16px; height: 16px; flex: none; }

  .brand {
    position: absolute; left: 22px; top: 140px;
    display: flex; align-items: center; gap: 7px;
  }
  .brand-dot { width: 18px; height: 18px; border-radius: 50%; background: var(--brand-red); }
  .brand-name {
    font-size: 13px; font-weight: 600; color: var(--brand-red);
    letter-spacing: 0.8px; text-transform: uppercase;
  }

  .back-brand {
    position: absolute; left: 0; right: 0; top: 270px;
    display: flex; align-items: center; justify-content: center; gap: 8px;
  }
  .back-brand .brand-dot { width: 34px; height: 34px; background: var(--brand-faint); }
  .back-brand .brand-name { font-size: 14px; color: var(--brand-faint); }
</style>
</head>
<body>
<main class="canvas">

  <section class="card card-front" aria-label="Card front">
    <svg class="wave" viewBox="0 0 560 320" preserveAspectRatio="none" aria-hidden="true">
      <path d="M0 196 C110 180 190 292 320 276 S 490 228 560 216 L560 320 L0 320 Z" fill="var(--wave-gold)"/>
      <path d="M0 208 C110 192 190 304 320 288 S 490 240 560 228 L560 320 L0 320 Z" fill="var(--wave-red)"/>
    </svg>

    <div class="holder">
      <h1 class="holder-name">Leo Park</h1>
      <p class="holder-title">Managing Director</p>
    </div>

    <ul class="contact-list">
      <li class="contact-item">
        <span>Suite 7/5 Harlow Rd Bayfield WA 6923</span>
        <svg class="contact-icon" viewBox="0 0 16 16" fill="none" stroke="var(--ink)" stroke-width="1.3"><path d="M2 8 L8 2.5 L14 8"/><path d="M3.5 7 V14 H12.5 V7"/><rect x="6.5" y="9.5" width="3" height="4.5"/></svg>
      </li>
      <li class="contact-item">
        <span>+61(8) 6027 3518</span>
        <svg class="contact-icon" viewBox="0 0 16 16" fill="var(--ink)"><path d="M3 2 h3 l1 3 -1.6 1.2 a8 8 0 0 0 4.4 4.4 L11 9 l3 1 v3 a1 1 0 0 1 -1 1 A11 11 0 0 1 2 3 a1 1 0 0 1 1 -1 z"/></svg>
      </li>
      <li class="contact-item">
        <span>lumocellar@lumocellartraders.example</span>
        <svg class="contact-icon" viewBox="0 0 16 16"><rect x="1" y="3" width="14" height="10" fill="var(--ink)"/><path d="M1 3 L8 9 L15 3 M1 13 L6 7.5 M15 13 L10 7.5" stroke="#fff" stroke-width="1.2" fill="none"/></svg>
      </li>
      <li class="contact-item">
        <span>www.lumocellartraders.example</span>
        <svg class="contact-icon" viewBox="0 0 16 16" fill="none" stroke="var(--ink)" stroke-width="1.1"><circle cx="8" cy="8" r="6.5"/><ellipse cx="8" cy="8" rx="3" ry="6.5"/><path d="M1.5 8 H14.5 M2.5 5 H13.5 M2.5 11 H13.5"/></svg>
      </li>
    </ul>

    <div class="brand">
      <span class="brand-dot" aria-hidden="true"></span>
      <span class="brand-name">Lumo Cellar Traders</span>
    </div>
  </section>

  <section class="card card-back" aria-label="Card back">
    <svg class="wave" viewBox="0 0 320 560" preserveAspectRatio="none" aria-hidden="true">
      <path d="M0 0 H320 V118 C255 90 170 40 0 26 Z" fill="var(--wave-gold)"/>
      <path d="M0 0 H320 V104 C255 78 170 30 0 18 Z" fill="var(--wave-red-light)"/>
    </svg>
    <div class="back-brand">
      <span class="brand-dot" aria-hidden="true"></span>
      <span class="brand-name">Lumo Cellar Traders</span>
    </div>
  </section>

</main>
</body>
</html>
```